BRAMLEIGH real estate family office

Hello, Our business is a real estate intermediation activity on high-end goods (amounts exceeding € 10m) for corporate and private clients. You can see our logo on the site www.bramleigh-invented.fr We would like to keep that spirit with the hexagon that represents France (transactions between Monaco and Saint Tropez, Courchevel and Paris). And the "baseline" that is "real estate family office". The corporate logo should be and can be printed by embossing (relief). We must integrate the name, first name, phone, email and website. Finally, to imbibe the spirit of business, here is a detail of the activity. "Genuine consulting firm in real estate investments, BRAMLEIGH works with its customers as a specialized player in the high-end markets, we are recognized for our ultra-confidential approach and tailor-made, as well as the quality of our network. We broadcast any information on the market and we work exclusively through a strong relationship we have developed over the years. BRAMLEIGH is active on the French Riviera (from Monaco to Saint-Tropez), the Alps (Courchevel, Méribel, Megève) and Paris (essentially market premium). Always looking for opportunities for our clients, we work on two investment areas: residential luxury real estate (properties, vineyards, mansions, land, etc.) commercial real estate (empty office buildings or yield, hotel properties, land, etc.) "

Target Market(s)

High foreign end customers. corporate and private.

Industry/Entity Type

Real Estate

Contact Information for Business Card

LOGO
baseline
Laurent Dufossé
+33(0)6.41.57.09.64
ld@bramleigh-invented.fr
www.bramleigh-invented.fr

Font styles to use
Serif

Colors
cedeed
0255a3
3277b5
85abd2
85cae6
34a7d7
0792cd
cfdeed
1b1b1b

Requirements
Must have
• see description

```html
<!DOCTYPE html>
<html lang="fr">
<head>
<meta charset="utf-8">
<title>Bramleigh – business card</title>
<link rel="stylesheet" href="https://fonts.googleapis.com/css2?family=Open+Sans:wght@300;400;600&display=swap">
<style>
  :root {
    --page-bg: #e6e6e6;
    --card-white: #f7f7f7;
    --card-white-edge: #ececec;
    --ink: #4a4a4a;
    --ink-soft: #5a5a5a;
    --navy: #232a7c;
    --navy-deep: #1e2470;
    --accent-blue: #2b3596;
    --sky: #6cb7e8;
    --rule-blue: #4aa8dc;
  }
  * { box-sizing: border-box; margin: 0; padding: 0; }
  html, body {
    width: 1200px;
    height: 443px;
    overflow: hidden;
    background: var(--page-bg);
    font-family: "Open Sans", Arial, sans-serif;
  }
  .canvas {
    position: relative;
    width: 1200px;
    height: 443px;
  }
  .card {
    position: absolute;
    top: 70px;
    width: 484px;
    height: 294px;
    overflow: hidden;
  }
  .card--front {
    left: 82px;
    background: linear-gradient(135deg, #ffffff 0%, var(--card-white) 55%, var(--card-white-edge) 100%);
  }
  .card--back {
    left: 602px;
    background: linear-gradient(160deg, var(--navy) 0%, var(--navy-deep) 100%);
  }

  .brand {
    position: absolute;
    display: inline-flex;
    flex-direction: column;
    align-items: flex-end;
  }
  .brand__name {
    font-weight: 300;
    font-size: 29px;
    line-height: 1;
    letter-spacing: 3px;
  }
  .brand__baseline {
    font-weight: 400;
    font-size: 9.5px;
    letter-spacing: 0.3px;
    margin-top: 3px;
    margin-right: 2px;
  }
  .card--front .brand { left: 34px; top: 44px; }
  .card--front .brand__name { color: var(--ink); }
  .card--front .brand__baseline { color: var(--accent-blue); }

  .card--back .brand { left: 186px; top: 128px; }
  .card--back .brand__name { color: var(--sky); }
  .card--back .brand__baseline { color: var(--sky); }

  .contact {
    position: absolute;
    left: 34px;
    top: 180px;
    color: var(--ink);
  }
  .contact__headline {
    display: flex;
    align-items: center;
    margin-bottom: 8px;
  }
  .contact__name {
    font-weight: 600;
    font-size: 16px;
    color: var(--ink);
  }
  .contact__role {
    font-weight: 400;
    font-size: 12px;
    color: var(--ink-soft);
    border-left: 1.5px solid var(--rule-blue);
    margin-left: 6px;
    padding-left: 5px;
    line-height: 18px;
  }
  .contact__line {
    font-weight: 400;
    font-size: 12.5px;
    line-height: 15.6px;
    color: var(--ink-soft);
  }
</style>
</head>
<body>
  <main class="canvas">
    <section class="card card--front" aria-label="Card front">
      <div class="brand">
        <span class="brand__name">BRAMLEIGH</span>
        <span class="brand__baseline">real estate family office</span>
      </div>
      <div class="contact">
        <div class="contact__headline">
          <span class="contact__name">Laurent Dufossé</span>
          <span class="contact__role">CEO</span>
        </div>
        <p class="contact__line">+33(0)6.41.57.09.64</p>
        <p class="contact__line">ld@bramleigh-invented.fr</p>
        <p class="contact__line">www.bramleigh-invented.fr</p>
      </div>
    </section>

    <section class="card card--back" aria-label="Card back">
      <div class="brand">
        <span class="brand__name">BRAMLEIGH</span>
        <span class="brand__baseline">real estate family office</span>
      </div>
    </section>
  </main>
</body>
</html>
```